Create an awesome website for a medical clinic

This is a new website for a doctor's office. The site should be clean and modern, easy to navigate.

This is a wellness clinic, we want to help our clients have a healthy, active lifestyle. It should be friendly and inviting, and easy for them to call or schedule an appointment.

The site should be responsive and designed using the attached Bootstrap 3 PSD.

We will provide stock photos, until then please use stock photos from:

photoharvestbin.net or
lumapicturevault.net (preferred)

Some example sites of clean and modern designs that we like:

https://tarnelspine.example/
http://walkpastjoints.example/
http://feelingbrisker.example/

Also attached is a temporary logo you can use.
Updates

Reason: Thank you everyone for your great designs - we need a little more time so I'm extending the project.

Need extra days to review

Also, the colors in the new logo I just linked to are the final colors of the logo, so feel free to use any complimentary colors to it.

Hi everyone, The boss wants to change the layout of the site a little bit - here's the revised layout: https://www.filecrate.example/s/q8vn31kd2pxe74rt/memo%2011_29_2017.pdf?dl=0 And the graphic assets you can use are here: https://www.filecrate.example/s/q8vn31kd2pxe74rt/memo%2011_29_2017.pdf?dl=0 Feel free to change the background color of the "topbar", and change the icons of the "why people trust us" if you want, these are just temporary placeholders. Thanks for your patience and hard work!

Target Market(s)

People seeking medical treatment (wellness clinic)

Industry/Entity Type

Doctor

Number of Pages Required

1 page

Font styles to use
Sans Serif

Colors
0592cd
33a6d7
abd037
9bcb3c

Requirements
Must have
• The home page should have: a strong hero image/slideshow, clinic phone number should be prominent and at the top of the page (in the nav), a "what to expect" section (this is like a FAQs section - see attachment), and a strong call to action (a button to call or schedule an appointment).
• The what to expect section is useful so that prospective clients can determine if we're a good fit for them or not. It's a basic, first-step pre-qualification block of information.
• Social media icons which links to our social media profiles should be included.
Nice to have
• - Link to 3 most recent blog entries
• - Testimonials
• - How a multilevel nav menu looks.

```html
<!DOCTYPE html>
<html lang="en">
<head>
<meta charset="utf-8">
<title>Willow Medical Clinic</title>
<link rel="stylesheet" href="https://fonts.googleapis.com/css2?family=Roboto:ital,wght@0,300;0,400;0,500;0,700;0,900;1,400&display=swap">
<style>
:root{
  --green:#2f9e4f;
  --navy:#1f3f6e;
  --ink:#33465e;
  --muted:#8b97a6;
  --line:#e6eaee;
  --footer:#17284a;
  --stage:#ffffff;
  --coat:#ffffff;
  --scrub:#cfe0ee;
  --skin:#ecd9cc;
}
*{box-sizing:border-box;margin:0;padding:0}
html,body{width:1200px;height:1200px;overflow:hidden;background:var(--stage);font-family:"Roboto",Arial,sans-serif;color:var(--ink)}
.stage{position:relative;width:1200px;height:1200px}
.page{position:absolute;left:446px;top:15px;width:960px;height:3660px;transform:scale(.3197);transform-origin:0 0;background:#fff;box-shadow:0 0 40px rgba(0,0,0,.15);overflow:hidden}
.topbar{height:40px;display:flex;align-items:center;justify-content:space-between;padding:0 60px;font-size:11px;color:var(--navy);border-bottom:1px solid var(--line)}
.socials{display:flex;gap:10px}
.socials span{width:13px;height:13px;border:1.5px solid #b9c2cc;border-radius:50%}
.nav{height:52px;display:flex;align-items:center;justify-content:space-between;padding:0 60px}
.brand{color:var(--green);font-weight:900;font-size:19px;line-height:1}
.brand small{display:block;font-size:7px;font-weight:900;letter-spacing:.5px;margin-top:2px}
.menu{display:flex;gap:34px;font-size:11px;color:var(--navy);align-items:center}

.hero{position:relative;height:418px;background:linear-gradient(90deg,#f4f5f7 0%,#eef1f4 50%,#e9eef2 100%)}
.hero-photo{position:absolute;right:0;top:0;width:640px;height:418px;
  background:
    radial-gradient(ellipse 90px 110px at 58% 22%,var(--skin) 0%,rgba(236,217,204,.5) 55%,transparent 75%),
    radial-gradient(ellipse 150px 170px at 58% 80%,var(--coat) 0%,rgba(255,255,255,.7) 60%,transparent 80%),
    radial-gradient(ellipse 70px 80px at 86% 36%,var(--skin) 0%,transparent 72%),
    radial-gradient(ellipse 110px 150px at 86% 82%,var(--scrub) 0%,transparent 78%),
    radial-gradient(ellipse 60px 70px at 30% 40%,var(--skin) 0%,transparent 72%),
    radial-gradient(ellipse 120px 150px at 32% 85%,var(--scrub) 0%,transparent 78%),
    radial-gradient(ellipse 55px 65px at 42% 36%,var(--skin) 0%,transparent 72%);}
.hero-copy{position:absolute;left:58px;top:220px}
.kicker{font-size:11px;color:var(--muted)}
.hero h1{font-weight:300;font-size:27px;line-height:1.2;color:var(--navy);margin:6px 0 16px}
.pill{display:inline-block;background:#fff;border-radius:20px;padding:10px 22px;font-size:10px;font-weight:700;color:var(--navy);box-shadow:0 2px 8px rgba(0,0,0,.08)}

.info{margin:-50px 37px 0;position:relative;height:175px;background:var(--green);color:#fff;display:grid;grid-template-columns:235px 245px 1fr;padding:28px 22px;font-size:10px}
.info h4{font-size:11px;font-weight:700;margin-bottom:14px;display:flex;gap:7px;align-items:center}
.row{display:flex;justify-content:space-between;margin-bottom:12px;padding-right:30px}
.crow{display:flex;gap:8px;margin-bottom:12px}
.form{display:grid;grid-template-columns:1fr 1fr 1fr;gap:12px 10px}
.field{border:1.5px solid rgba(255,255,255,.85);border-radius:16px;height:28px;padding:8px 12px;font-size:9px}
.field.wide{grid-column:span 2}
.send{background:#fff;color:var(--green);border-radius:16px;height:28px;text-align:center;font-weight:700;padding-top:9px;font-size:9px}

.about{position:relative;height:575px;padding:70px 60px 0}
.sec-title{font-size:22px;font-weight:400;color:var(--navy)}
.sec-title::after{content:"";display:block;width:38px;height:3px;background:var(--green);margin-top:8px}
.center{text-align:center}
.center::after{margin:8px auto 0}
.about p{font-size:10px;line-height:1.45;width:410px;margin-top:16px;color:#4a5a6d}
.quote{font-size:20px;font-weight:300;color:#6f8aa7;margin:28px 0 24px}
.feat{width:410px;margin-bottom:38px}
.feat-head{display:flex;align-items:center;gap:12px;font-size:11px;font-weight:700;color:var(--navy)}
.feat-head .arr{margin-left:auto;color:var(--muted);font-weight:400}
.feat p{width:370px;margin:12px 0 0 38px}
.about-photo{position:absolute;right:40px;top:40px;width:380px;height:535px;
  background:
    radial-gradient(ellipse 55px 70px at 52% 16%,var(--skin) 0%,rgba(236,217,204,.4) 60%,transparent 78%),
    radial-gradient(ellipse 130px 190px at 50% 55%,var(--coat) 0%,rgba(255,255,255,.8) 60%,transparent 82%),
    radial-gradient(ellipse 70px 90px at 50% 92%,#c9ccc8 0%,transparent 75%),
    radial-gradient(ellipse 190px 270px at 50% 55%,#eef1f4 0%,transparent 85%);}

.facilities{height:344px;padding-top:60px}
.fac-grid{display:grid;grid-template-columns:repeat(6,1fr);margin:36px 60px 0;text-align:center}
.fac{padding:14px 6px 18px}
.fac.active{box-shadow:0 4px 18px rgba(0,0,0,.09)}
.fac svg{width:56px;height:56px}
.fac b{display:block;font-size:12px;font-weight:500;color:var(--navy);margin-top:12px}
.fac span{display:block;font-size:9px;color:var(--muted);margin-top:4px;line-height:1.3}
.stats{height:174px;background:var(--green);display:grid;grid-template-columns:repeat(4,1fr);color:#fff;text-align:center;padding:58px 60px 0}
.stats b{display:block;font-size:24px;font-weight:500}
.stats span{font-size:9px}

.news{height:450px;padding-top:58px}
.news-grid{display:grid;grid-template-columns:repeat(4,1fr);gap:22px;margin:36px 60px 0}
.card{box-shadow:0 3px 14px rgba(0,0,0,.07);padding-bottom:16px}
.card .img{height:175px}
.card h5{font-size:11px;color:var(--navy);margin:14px 14px 6px}
.card small{display:block;font-size:8px;color:var(--muted);margin:0 14px 10px}
.card p{font-size:8.5px;color:#5c6a7a;margin:0 14px;line-height:1.4}
.card .go{margin:10px 14px 0;font-size:11px;color:var(--muted)}

.testi{position:relative;height:397px;padding:60px 60px 0;background:linear-gradient(180deg,#fff 0%,#f4f6f8 100%)}
.testi .sec-title{font-size:18px;font-weight:400}
.headline{font-size:37px;font-weight:900;color:var(--navy);line-height:1.1;margin-top:34px}
.qm{position:absolute;left:420px;top:128px;font-size:70px;color:#c6ccd3;font-weight:900;line-height:1}
.testi em{display:block;font-size:9.5px;color:#7a8798;width:340px;margin-top:22px;line-height:1.45}
.who{font-size:9px;color:var(--navy);margin-top:22px}
.who span{color:var(--muted)}
.dots{display:flex;gap:7px;margin-top:14px;align-items:center}
.dots i{width:8px;height:8px;border-radius:50%;background:#cfd6dd}
.dots i.on{background:var(--navy)}
.dots .arr{margin-left:60px;font-size:12px;color:var(--muted)}
.testi-photo{position:absolute;right:60px;bottom:0;width:420px;height:330px;
  background:
    radial-gradient(ellipse 50px 62px at 50% 22%,var(--skin) 0%,rgba(236,217,204,.4) 60%,transparent 78%),
    radial-gradient(ellipse 170px 120px at 50% 82%,var(--coat) 0%,rgba(255,255,255,.8) 60%,transparent 82%),
    radial-gradient(ellipse 40px 45px at 18% 52%,var(--skin) 0%,transparent 75%),
    radial-gradient(ellipse 40px 45px at 82% 52%,var(--skin) 0%,transparent 75%);}

.faq{height:588px;padding:60px 60px 0}
.faq .sec-title{font-size:18px}
.qa{box-shadow:0 3px 14px rgba(0,0,0,.08);padding:24px 30px;margin-top:18px;font-size:10px;font-weight:700;color:var(--navy);display:flex;justify-content:space-between}
.qa.first{margin-top:30px}
.qa.open{display:block;padding-bottom:26px}
.qa.open .q{display:flex;justify-content:space-between}
.qa p{font-weight:400;color:#6b7888;font-size:8.5px;margin-top:10px;line-height:1.4;width:780px}
.qa span{color:var(--muted);font-weight:400}
.map{height:469px;background:
  radial-gradient(ellipse 140px 200px at 18% 20%,#8fb6e0 0%,#b9d1ea 50%,transparent 75%),
  linear-gradient(135deg,#e9ecef 0%,#f1f3f5 50%,#e3e7eb 100%);position:relative}
.pin{position:absolute;left:467px;top:200px}
.footer{height:43px;background:var(--footer);color:#fff;font-size:10px;text-align:center;padding-top:15px}
</style>
</head>
<body>
<div class="stage">
  <div class="page">
    <div class="topbar">
      <span>For Emergency call 555.014.2290</span>
      <div class="socials"><span></span><span></span><span></span><span></span></div>
    </div>
    <header class="nav">
      <div class="brand">WILLOW<small>MEDICAL CLINIC</small></div>
      <nav class="menu">
        <span>About Me</span><span>Medical Services</span><span>Departments</span><span>What to Expect</span><span>Contact</span>
        <svg width="12" height="12" viewBox="0 0 12 12"><circle cx="5" cy="5" r="4" fill="none" stroke="#9aa6b2" stroke-width="1.4"/><line x1="8" y1="8" x2="11" y2="11" stroke="#9aa6b2" stroke-width="1.4"/></svg>
      </nav>
    </header>

    <section class="hero">
      <div class="hero-photo" role="img" aria-label="Smiling team of doctors and nurses in white coats"></div>
      <div class="hero-copy">
        <div class="kicker">Suas munere corrumpit te quo</div>
        <h1>Persius ponderum honestati<br>squod postea vocent</h1>
        <span class="pill">WHAT TO EXPECT</span>
      </div>
    </section>

    <section class="info">
      <div>
        <h4><svg width="10" height="10"><circle cx="5" cy="5" r="4.5" fill="#fff"/></svg>Working Time</h4>
        <div class="row"><span>Monday - Friday</span><span>8.00 - 17.00</span></div>
        <div class="row"><span>Saturday</span><span>9.30 - 17.30</span></div>
        <div class="row"><span>Sunday</span><span>9.30 - 15.30</span></div>
      </div>
      <div>
        <h4><svg width="10" height="10" viewBox="0 0 10 10"><path d="M2 1l2 2-1 1.5c.8 1.4 1.5 2.1 2.5 2.5L7 6l2 2-1.5 1.5C4 9 1 6 .5 2.5z" fill="#fff"/></svg>Contact Us</h4>
        <div class="crow"><span>✆</span>555.014.2290</div>
        <div class="crow"><span>✉</span>contact@willowclinic.example</div>
        <div class="crow"><span>⌂</span>48 Alder Row, Brookfield, NY 10410</div>
      </div>
      <div>
        <h4><svg width="8" height="10" viewBox="0 0 8 10"><path d="M4 0a4 4 0 0 1 4 4c0 3-4 6-4 6S0 7 0 4a4 4 0 0 1 4-4z" fill="#fff"/></svg>Booking a visit</h4>
        <div class="form">
          <div class="field">Full Name</div><div class="field">Phone</div><div class="field">Date of Birth</div>
          <div class="field wide">Reason</div><div class="send">SEND</div>
        </div>
      </div>
    </section>

    <section class="about">
      <h2 class="sec-title">About Me</h2>
      <p>Id mollis instructior sit, his fuisset democritum ex, nibh docendi legendos ne sit. Eum diceret indoctum eam Persius ponor sit, his fuisset democritum ex, nibh docendi legendos neum deum honestatis vel ad, quod postea vocent no vel.</p>
      <div class="quote">“Health is the most preciuos treasure”</div>
      <div class="feat">
        <div class="feat-head"><svg width="18" height="18" viewBox="0 0 18 18"><circle cx="9" cy="6" r="4.5" fill="#1f3f6e"/><path d="M2 18c0-5 3-7 7-7s7 2 7 7z" fill="#1f3f6e"/></svg>Experienced Physician<span class="arr">↑</span></div>
        <p>Lorem ipsum dolor sit amet, cu decore efficiantur vis, possim melius vel ad. Ei vidisse minimum inciderint mei, an iusto corrumpit voluptatibus nec, eos pa rtem placerat disputationi in. Justo dicant doctus sed in, sit putent diceret an, ludus ubique no nam. In veri decore dictas sit, nam eu nisl possit, pri erat placerat patrioque id.</p>
      </div>
      <div class="feat">
        <div class="feat-head"><svg width="18" height="18" viewBox="0 0 18 18"><path d="M3 15L14 4l1.5 1.5L4.5 16.5z" fill="#1f3f6e"/><path d="M14 2l2 2" stroke="#1f3f6e" stroke-width="2"/></svg>Complete Health Facilities<span class="arr">→</span></div>
      </div>
      <div class="feat">
        <div class="feat-head"><svg width="18" height="18" viewBox="0 0 18 18"><rect x="1" y="3" width="16" height="10" fill="#1f3f6e"/><rect x="7" y="13" width="4" height="3" fill="#1f3f6e"/><path d="M3 8h3l1.5-3 2 5 1.5-2h4" stroke="#fff" fill="none" stroke-width="1.2"/></svg>Medical Standard Equipment<span class="arr">→</span></div>
      </div>
      <div class="about-photo" role="img" aria-label="Doctor in white coat with stethoscope holding a clipboard"></div>
    </section>

    <section class="facilities">
      <h2 class="sec-title center">Facilities</h2>
      <div class="fac-grid">
        <div class="fac"><svg viewBox="0 0 56 56"><rect x="8" y="16" width="28" height="14" rx="7" transform="rotate(-45 22 23)" fill="#2f9e4f"/><circle cx="36" cy="36" r="11" fill="#2f9e4f"/><line x1="36" y1="25" x2="36" y2="47" stroke="#fff" stroke-width="2"/></svg><b>Medicines</b><span>Id mollis instructior<br>sit, his fuisset</span></div>
        <div class="fac"><svg viewBox="0 0 56 56"><path d="M28 46C12 34 6 26 6 18a10 10 0 0 1 22-3 10 10 0 0 1 22 3c0 8-6 16-22 28z" fill="#2f9e4f"/><path d="M8 26h12l4-7 5 13 4-6h15" stroke="#fff" stroke-width="2.5" fill="none"/></svg><b>Best Care</b><span>Id mollis instructior<br>sit, his fuisset</span></div>
        <div class="fac"><svg viewBox="0 0 56 56"><rect x="20" y="8" width="16" height="8" rx="2" fill="none" stroke="#2f9e4f" stroke-width="3"/><rect x="6" y="14" width="44" height="32" rx="4" fill="#2f9e4f"/><circle cx="28" cy="30" r="10" fill="#fff"/><path d="M28 24v12M22 30h12" stroke="#2f9e4f" stroke-width="3"/></svg><b>Research</b><span>Id mollis instructior<br>sit, his fuisset</span></div>
        <div class="fac active"><svg viewBox="0 0 56 56"><rect x="5" y="14" width="4" height="30" fill="#2f9e4f"/><rect x="5" y="34" width="46" height="5" fill="#2f9e4f"/><rect x="47" y="30" width="4" height="14" fill="#2f9e4f"/><circle cx="16" cy="28" r="5" fill="#2f9e4f"/><rect x="23" y="26" width="24" height="7" fill="#2f9e4f"/><path d="M36 8v12M30 14h12" stroke="#2f9e4f" stroke-width="4"/></svg><b>Bed Facility</b><span>Id mollis instructior<br>sit, his fuisset</span></div>
        <div class="fac"><svg viewBox="0 0 56 56"><rect x="17" y="6" width="22" height="7" fill="#2f9e4f"/><rect x="15" y="15" width="26" height="35" rx="3" fill="#2f9e4f"/><rect x="19" y="23" width="18" height="18" fill="#fff"/><path d="M28 26v12M22 32h12" stroke="#2f9e4f" stroke-width="3"/></svg><b>Safe Medication</b><span>Id mollis instructior<br>sit, his fuisset</span></div>
        <div class="fac"><svg viewBox="0 0 56 56"><rect x="13" y="10" width="30" height="40" rx="3" fill="#2f9e4f"/><rect x="21" y="6" width="14" height="8" rx="2" fill="#2f9e4f" stroke="#fff" stroke-width="1.5"/><path d="M19 24h18M19 31h18M19 38h12" stroke="#fff" stroke-width="2.5"/></svg><b>Reports</b><span>Id mollis instructior<br>sit, his fuisset</span></div>
      </div>
    </section>

    <section class="stats">
      <div><b>200%</b><span>Trustworthy</span></div>
      <div><b>2451</b><span>Patients in a year</span></div>
      <div><b>215</b><span>Awards Won</span></div>
      <div><b>24</b><span>Years of Experience</span></div>
    </section>

    <section class="news">
      <h2 class="sec-title center">Latest News</h2>
      <div class="news-grid">
        <article class="card"><div class="img" role="img" aria-label="Park bench among trees" style="background:linear-gradient(180deg,#8a9a7a,#4e5a44)"></div><h5>First day in hospital</h5><small>10 Dec, 2017</small><p>Eum diceret indoctum ei. Persius ponderum honestatis vel ad, quod postea vocent no vel.</p><div class="go">→</div></article>
        <article class="card"><div class="img" role="img" aria-label="Young girl smiling outdoors" style="background:linear-gradient(180deg,#b9ae94,#8d8a6e)"></div><h5>First day in hospital</h5><small>10 Dec, 2017</small><p>Eum diceret indoctum ei. Persius ponderum honestatis vel ad, quod postea vocent no vel.</p><div class="go">→</div></article>
        <article class="card"><div class="img" role="img" aria-label="Child standing in green garden" style="background:linear-gradient(180deg,#5f8a4a,#2f5a2a)"></div><h5>First day in hospital</h5><small>10 Dec, 2017</small><p>Eum diceret indoctum ei. Persius ponderum honestatis vel ad, quod postea vocent no vel.</p><div class="go">→</div></article>
        <article class="card"><div class="img" role="img" aria-label="Swimmer in blue pool water" style="background:linear-gradient(180deg,#5fb7c9,#2f8aa3)"></div><h5>First day in hospital</h5><small>10 Dec, 2017</small><p>Eum diceret indoctum ei. Persius ponderum honestatis vel ad, quod postea vocent no vel.</p><div class="go">→</div></article>
      </div>
    </section>

    <section class="testi">
      <h2 class="sec-title">Testimonials</h2>
      <h3 class="headline">KEEP YOUR HEAD UP<br>AND BE PATIENT</h3>
      <div class="qm">”</div>
      <em>Justo dicant doctus sed in, sit putent diceret an, ludus ubique no nam. In veri decore dictas sit, nam eu nisl possit, pri erat placerat mollis instructior sit, his fuisset democritum ex, nibh docendi legendos ne sit.</em>
      <div class="who">Owen Marlow, <span>Happy Patient</span></div>
      <div class="dots"><i></i><i></i><i class="on"></i><i></i><span class="arr">→</span></div>
      <div class="testi-photo" role="img" aria-label="Cheerful man in shirt and tie giving two thumbs up"></div>
    </section>

    <section class="faq">
      <h2 class="sec-title center">FAQ</h2>
      <div class="qa open first"><div class="q">Id mollis instructior sit, his fuisset democritum ex, nibh docendi legendos ne sit?<span>↑</span></div><p>Justo dicant doctus sed in, sit putent diceret an, ludus ubique no nam. In veri decore dictas sit, nam eu nisl possit, pri erat placerat patrioque id. Id mollis instructior sit, his fuisset democritum ex, nibh docendi legendos ne sit. Eum diceret indoctum ei. Persius ponderum honestatis vel ad, quod postea vocent no vel. Cu eos dicam utinam voluptatum.</p></div>
      <div class="qa">Eu cum eligendi voluptua perfecto. No brute laboramus reprehendunt pri, et sint ponderum quo?<span>→</span></div>
      <div class="qa">Quo omnis voluptaria ut, causae habemus ius at. Duo in etiam numquam lobortis, sed ne eligendi cotidieque?<span>→</span></div>
      <div class="qa">Suas munere corrumpit te quo, duo salutatus voluptatibus definitionem at?<span>→</span></div>
      <div class="qa">Justo dicant doctus sed in, sit putent diceret an, ludus ubique no nam. In veri decore dictas sit, nam eu nisi?<span>→</span></div>
    </section>

    <section class="map" role="img" aria-label="Street map of the clinic neighbourhood with waterfront">
      <svg class="pin" width="26" height="34" viewBox="0 0 26 34"><path d="M13 0a13 13 0 0 1 13 13c0 9-13 21-13 21S0 22 0 13A13 13 0 0 1 13 0z" fill="#1f6fb5"/><circle cx="13" cy="12" r="5" fill="#fff"/></svg>
    </section>

    <footer class="footer">© 2017 Copyright Willow</footer>
  </div>
</div>
</body>
</html>
```